TwistyLanesCamp.com

Current website needs redesign to make it more attractive and easier to Navigate. Currently being hosted on net porter. Can be accessed at
www,twistylanescamp.com.

```html
<!DOCTYPE html>
<html lang="en">
<head>
<meta charset="utf-8">
<title>Twisty Lanes Camp</title>
<link href="https://fonts.googleapis.com/css2?family=Poppins:wght@300;400;500;600;700;800&family=Lato:wght@400;700&display=swap" rel="stylesheet">
<style>
:root{
  --red:#c8102e;
  --red-dark:#a50d26;
  --ink:#1d1d1f;
  --text:#333;
  --muted:#777;
  --dark:#1a1a1a;
  --white:#fff;
  --line:#e3e3e3;
}
*{box-sizing:border-box;margin:0;padding:0}
html,body{width:1200px;height:3929px;overflow:hidden}
body{position:relative;font-family:"Lato",sans-serif;color:var(--text);background:var(--white)}
.abs{position:absolute}
.brand{display:flex;align-items:center;gap:10px;font-family:"Poppins",sans-serif;font-weight:700;color:var(--ink)}
.brand-mark{width:26px;height:26px;background:var(--red)}
/* header */
.topbar-item{display:flex;align-items:center;gap:18px;font-size:17px;color:var(--text)}
.topbar-icon{width:60px;height:44px;background:var(--red);display:flex;align-items:center;justify-content:center;clip-path:polygon(10% 0,100% 0,90% 100%,0 100%)}
.nav{left:365px;top:80px;width:835px;height:48px;background:var(--red);clip-path:polygon(40px 0,100% 0,100% 100%,0 100%)}
.nav ul{list-style:none;display:flex;gap:27px;position:absolute;left:47px;top:15px}
.nav li{color:var(--white);font-size:13.5px;font-family:"Poppins",sans-serif}
.nav li.active{border-bottom:2px solid var(--white);padding-bottom:10px}
/* buttons */
.btn{display:inline-block;background:var(--red);color:var(--white);font-family:"Poppins",sans-serif;font-weight:600;font-size:15px;padding:16px 26px;box-shadow:6px 0 0 var(--dark);clip-path:polygon(6px 0,100% 0,calc(100% - 6px) 100%,0 100%)}
.btn.light{background:var(--white);color:var(--red)}
/* hero */
.photo{position:absolute}
.hero-title-sm{left:111px;top:258px;font-family:"Poppins",sans-serif;font-size:52px;font-weight:400;color:var(--red);letter-spacing:1px}
.hero-title{left:108px;top:318px;font-family:"Poppins",sans-serif;font-size:82px;font-weight:800;color:var(--white);letter-spacing:1px}
.hero-text{left:111px;top:420px;width:400px;color:var(--white);font-size:15.5px;line-height:26px}
/* section label */
.eyebrow{display:flex;align-items:center;gap:10px;color:var(--red);font-family:"Poppins",sans-serif;font-weight:600;font-size:14px}
.swoosh{width:32px;height:10px}
.sec-title{font-family:"Poppins",sans-serif;font-size:30px;font-weight:400;color:var(--ink)}
.sec-title b{color:var(--red);font-weight:700}
.about-text{left:598px;top:898px;width:490px;font-size:15px;line-height:25.7px;color:var(--text)}
/* women circle */
.circle{left:638px;top:1405px;width:430px;height:430px;border-radius:50%;background:rgba(200,16,46,.93);text-align:center;color:var(--white)}
.circle h3{font-family:"Poppins",sans-serif;font-weight:300;font-size:30px;margin-top:80px;line-height:44px}
.circle h3 b{font-weight:700}
.circle p{font-size:14.5px;line-height:26px;width:340px;margin:22px auto 26px}
/* blog */
.card{position:absolute;top:2187px;width:310px;height:453px;background:var(--white);box-shadow:0 4px 14px rgba(0,0,0,.12);border-bottom:3px solid var(--red)}
.card .thumb{height:213px}
.card .body{padding:28px 22px 0}
.date{display:flex;align-items:center;gap:9px;color:var(--red);font-family:"Poppins",sans-serif;font-size:16px;font-weight:500}
.card h4{font-family:"Poppins",sans-serif;font-weight:500;font-size:17.5px;line-height:26px;letter-spacing:-.2px;color:var(--ink);margin:14px 0 12px}
.card p{font-size:14.5px;line-height:25px;color:var(--text)}
.card a{position:absolute;left:22px;bottom:30px;color:var(--red);font-family:"Poppins",sans-serif;font-weight:500;font-size:15px;text-decoration:underline}
/* form */
.field{position:absolute;background:var(--white);color:#777;font-size:15px;padding:20px 16px}
/* footer */
.foot-col h5{font-family:"Poppins",sans-serif;font-weight:500;font-size:18px;color:var(--ink);margin-bottom:12px}
.foot-col li{list-style:none;color:var(--muted);font-size:15px;line-height:26px}
.social{display:flex;gap:15px}
.social span{width:40px;height:40px;border-radius:50%;background:#4a4a4a}
</style>
</head>
<body>

<header>
  <div class="abs brand" style="left:111px;top:48px;font-size:25px"><span class="brand-mark"></span>TwistyLanesCamp.com</div>
  <div class="abs topbar-item" style="left:400px;top:18px"><span class="topbar-icon"><svg width="20" height="20" viewBox="0 0 24 24"><path fill="#fff" d="M6.6 10.8a15 15 0 0 0 6.6 6.6l2.2-2.2c.3-.3.7-.4 1-.2 1.1.4 2.3.6 3.6.6.6 0 1 .4 1 1V20c0 .6-.4 1-1 1A17 17 0 0 1 3 4c0-.6.4-1 1-1h3.5c.6 0 1 .4 1 1 0 1.3.2 2.5.6 3.6.1.3 0 .7-.2 1z"/></svg></span>Phone:&nbsp;(555) 014 2290</div>
  <div class="abs" style="left:702px;top:25px;width:1px;height:30px;background:#ccc"></div>
  <div class="abs topbar-item" style="left:758px;top:18px"><span class="topbar-icon"><svg width="22" height="16" viewBox="0 0 24 18"><path fill="#fff" d="M0 0h24v2L12 10 0 2zM0 4l12 8 12-8v14H0z"/></svg></span>Email:&nbsp;<b>info@twistylanescamp.com</b></div>
  <nav class="abs nav"><ul>
    <li class="active">Home</li><li>About</li><li>Trails &amp; Tales</li><li>The Smart Rver</li><li>Women on the Road</li><li>Bad RV</li><li>Blog</li><li>Contact</li>
  </ul></nav>
</header>

<section>
  <div class="photo" role="img" aria-label="Highway through green mountains with a branded white semi-truck passing" style="left:0;top:130px;width:1200px;height:600px;background:linear-gradient(100deg,#5c6a5a 0%,#7b8a76 30%,#8e8a82 50%,#d9d9d9 70%,#f1f1f1 100%)"></div>
  <svg class="abs" style="left:0;top:600px" width="1200" height="130" viewBox="0 0 1200 130">
    <polygon points="0,90 1200,10 1200,130 0,130" fill="#fff"/>
    <polygon points="0,90 1200,10 1200,48 0,125" fill="var(--red)"/>
  </svg>
  <div class="abs hero-title-sm">WELCOME TO</div>
  <div class="abs hero-title">TWISTY LANES</div>
  <p class="abs hero-text">If you're anxious for more fun and fewer bumps on the road to adventure, we can help!</p>
  <div class="abs" style="left:115px;top:495px"><span class="btn">GET STARTED</span></div>
  <div class="abs" style="left:570px;top:640px;width:60px;height:60px;border-radius:50%;background:#fff;box-shadow:0 2px 8px rgba(0,0,0,.25);display:flex;align-items:center;justify-content:center">
    <svg width="20" height="34" viewBox="0 0 20 34"><path d="M10 2v28M3 22l7 9 7-9" stroke="var(--ink)" stroke-width="2.5" fill="none"/></svg>
  </div>
</section>

<section>
  <div class="photo" role="img" aria-label="Motorhome parked at a site" style="left:147px;top:810px;width:361px;height:318px;background:linear-gradient(135deg,#c9c9c9,#3b3b3b)"></div>
  <div class="photo" role="img" aria-label="Truck driving on a highway at sunset" style="left:53px;top:905px;width:361px;height:315px;background:linear-gradient(180deg,#a7a5a6 0%,#c3a48a 45%,#4d4c4b 100%)"></div>
  <div class="abs" style="left:113px;top:845px;width:361px;height:315px;border:3px solid var(--red)"></div>
  <div class="abs eyebrow" style="left:598px;top:810px"><svg class="swoosh" viewBox="0 0 32 10"><path d="M0 10 Q14 0 32 0 Q16 3 2 10z" fill="var(--red)"/></svg>ABOUT US</div>
  <h2 class="abs sec-title" style="left:598px;top:843px">WELCOME TO <b>TWISTY LANES</b></h2>
  <p class="abs about-text">We are primarily an educational and advisory website dedicated to helping other RVers make less mistakes and take fewer missteps on their journey to adventure. Our Smart RVer section is dedicated to giving our readers tips and advice on making the Rv journey an easier one. We will use the “wisdom of the crowd”, namely you our readers, to provide much of the content for this section. Our combined experience on the road is significant and we have all learned from this experience. We are less interested in pushing particular products, or tools or RV's on our site.</p>
  <div class="abs" style="left:601px;top:1160px"><span class="btn">LEARN MORE</span></div>
</section>

<section>
  <div class="photo" role="img" aria-label="Woman with a backpack standing by an empty mountain road" style="left:0;top:1295px;width:1200px;height:690px;background:linear-gradient(100deg,#4b5445 0%,#6d7665 40%,#8a8f86 65%,#6f7670 100%)"></div>
  <svg class="abs" style="left:0;top:1295px" width="1200" height="690" viewBox="0 0 1200 690">
    <polygon points="0,0 1200,0 1200,0 0,60" fill="#fff"/>
    <polygon points="0,60 1200,0 1200,12 0,72" fill="var(--dark)"/>
    <polygon points="0,665 1200,580 1200,690 0,690" fill="#fff"/>
    <polygon points="0,665 1200,580 1200,592 0,690" fill="var(--red)"/>
    <g fill="none" stroke="#fff" stroke-width="4"><rect x="848" y="22" width="10" height="22"/><rect x="848" y="58" width="10" height="22"/><rect x="848" y="94" width="10" height="22"/></g>
  </svg>
  <div class="abs circle">
    <h3>WOMEN ON<br><b>THE ROAD</b></h3>
    <p>When we talk to couples on the road, especially Motorhome ...Duct Tales: Never Leave Home Without IT!Whew....just finished another article, need a breakLadies and Gents....you ...</p>
    <span class="btn light">LEARN MORE</span>
  </div>
</section>

<section>
  <h2 class="abs sec-title" style="left:0;width:1200px;top:2055px;text-align:center"><svg width="52" height="16" viewBox="0 0 52 16" style="vertical-align:middle"><path d="M0 16 Q22 0 52 2 Q26 4 4 16z" fill="var(--red)"/><path d="M6 16 Q26 6 52 6" stroke="var(--dark)" stroke-width="1.5" fill="none"/></svg>FEATURED <b>BLOG POSTS</b></h2>
  <p class="abs" style="left:0;width:1200px;top:2110px;text-align:center;font-size:15px">There are lots of positive comments about Glide Coil suspension ...</p>

  <article class="card" style="left:111px">
    <div class="thumb" role="img" aria-label="Camper van parked under a starry night sky" style="background:linear-gradient(160deg,#1d2a44,#5d5a55)"></div>
    <div class="body">
      <div class="date"><svg width="20" height="20" viewBox="0 0 20 20"><circle cx="10" cy="10" r="8" fill="none" stroke="var(--red)" stroke-width="2"/><path d="M10 5v5l3 2" stroke="var(--red)" stroke-width="2" fill="none"/></svg>Dec 11,2021</div>
      <h4>RV Envy? Why you will<br>always want a different one!</h4>
      <p>When my wife and I settle into a campground, we like to walk around</p>
    </div>
    <a>Learn More</a>
  </article>
  <article class="card" style="left:445px">
    <div class="thumb" role="img" aria-label="Dark pickup truck at dusk" style="background:linear-gradient(180deg,#8a5a44,#2a2423)"></div>
    <div class="body">
      <div class="date"><svg width="20" height="20" viewBox="0 0 20 20"><circle cx="10" cy="10" r="8" fill="none" stroke="var(--red)" stroke-width="2"/><path d="M10 5v5l3 2" stroke="var(--red)" stroke-width="2" fill="none"/></svg>Dec 11,2021</div>
      <h4>Class A Motorhomes: Prepare<br>for a love hate relationship</h4>
      <p>My wife and I have owned two class A motorhomes: one a new 37 ft.</p>
    </div>
    <a>Learn More</a>
  </article>
  <article class="card" style="left:779px">
    <div class="thumb" role="img" aria-label="Campground with palm trees and camp chairs" style="background:linear-gradient(180deg,#b9c6d2,#6b6d63)"></div>
    <div class="body">
      <div class="date"><svg width="20" height="20" viewBox="0 0 20 20"><circle cx="10" cy="10" r="8" fill="none" stroke="var(--red)" stroke-width="2"/><path d="M10 5v5l3 2" stroke="var(--red)" stroke-width="2" fill="none"/></svg>Dec 11,2021</div>
      <h4>RV Hell: Driving off without<br>your wife!</h4>
      <p>It was a steady downpour that day in rural Mississippi.</p>
    </div>
    <a>Learn More</a>
  </article>
</section>

<section>
  <div class="photo" role="img" aria-label="Forest road with a branded white pickup truck" style="left:0;top:2720px;width:1200px;height:700px;background:linear-gradient(100deg,#3a4532 0%,#5b6a49 45%,#8a8f84 70%,#55604a 100%)"></div>
  <svg class="abs" style="left:0;top:2715px" width="1200" height="760" viewBox="0 0 1200 760">
    <polygon points="0,0 1200,0 0,75" fill="#fff"/>
    <polygon points="0,75 1200,0 1200,12 0,90" fill="var(--dark)"/>
    <polygon points="0,680 1200,590 1200,760 0,760" fill="#fff"/>
    <polygon points="0,680 1200,590 1200,605 0,700" fill="var(--red)"/>
  </svg>
  <h2 class="abs" style="left:111px;top:2838px;font-family:'Poppins',sans-serif;font-size:30px;font-weight:400;color:#fff"><svg width="52" height="16" viewBox="0 0 52 16" style="vertical-align:middle;margin-right:6px"><path d="M0 16 Q22 0 52 2 Q26 4 4 16z" fill="#fff"/></svg>WOMEN ON <b style="font-weight:700">THE ROAD</b></h2>
  <div class="field" style="left:111px;top:2905px;width:280px;height:60px">Name*</div>
  <div class="field" style="left:407px;top:2905px;width:280px;height:60px">Phone*</div>
  <div class="field" style="left:111px;top:2985px;width:280px;height:60px">Email*</div>
  <div class="field" style="left:407px;top:2985px;width:280px;height:60px">Subject*</div>
  <div class="field" style="left:111px;top:3068px;width:576px;height:110px">Message</div>
  <div class="abs" style="left:115px;top:3205px"><span class="btn">SUBMIT NOW</span></div>
</section>

<footer>
  <div class="abs brand" style="left:111px;top:3640px;font-size:22px"><span class="brand-mark"></span>TwistyLanesCamp.com</div>
  <div class="abs foot-col" style="left:457px;top:3548px"><h5>QUICK LINKS</h5><ul><li>Home</li><li>About</li><li>Trails &amp; Tales</li><li>The Smart Rver</li><li>Women on the Road</li><li>Bad RV</li><li>Blog</li><li>Contact</li></ul></div>
  <div class="abs foot-col" style="left:650px;top:3548px"><h5>OUR COMPANY</h5><ul><li>Terms&amp;condtions</li><li>Privacy Policy</li><li>About Us</li><li>Support</li></ul></div>
  <div class="abs foot-col" style="left:853px;top:3548px;width:240px">
    <h5>EMAIL</h5><ul><li>info@twistylanescamp.com</li></ul>
    <h5 style="margin-top:22px">PHONE</h5><ul><li>(555) 014 2290</li></ul>
    <h5 style="margin-top:22px">ADDRESS</h5><ul><li>123, Lorem ipsum dolor sit amet, consectetur adipiscing elit,</li></ul>
  </div>
  <div class="abs" style="left:111px;top:3835px;width:978px;height:1px;background:var(--red)"></div>
  <p class="abs" style="left:111px;top:3872px;font-size:14.5px;color:var(--muted)">©Copyrights 2021 Company Name &nbsp;| &nbsp; All Rights Reserved</p>
  <div class="abs social" style="left:874px;top:3862px" aria-label="Social links"><span></span><span></span><span></span><span></span></div>
</footer>

</body>
</html>
```